ESCORT DIRECTORY

This website is an advertising and information resource , we only sell advertisement space.
The requirement:
-- 7 Banners with different size
--sexy girl on the banner
-- the sexy girl will have different position on each banner
--I want my logo on the banner (Upload files)
-- I want the word : " ADVERTISE FOR FREE" in a beautiful presentation

```html
<!DOCTYPE html>
<html lang="en">
<head>
<meta charset="UTF-8">
<title>Escort Directory Banner</title>
<link href="https://fonts.googleapis.com/css2?family=Josefin+Sans:wght@300&family=Montserrat:wght@600;700&display=swap" rel="stylesheet">
<style>
  :root {
    --bg-light: #fff4f8;
    --bg-blush: #fbd9e8;
    --pink: #ff2f8f;
    --pink-deep: #e8197a;
    --satin-light: #ff9cc9;
    --satin-mid: #f25aa3;
    --satin-dark: #b8266d;
    --ink: #111111;
    --logo-ink: #4a4a4a;
    --white: #ffffff;
  }
  * { margin: 0; padding: 0; box-sizing: border-box; }
  html, body {
    width: 1200px;
    height: 148px;
    overflow: hidden;
    background: var(--white);
  }
  .banner {
    position: relative;
    width: 1200px;
    height: 148px;
    overflow: hidden;
    background: linear-gradient(90deg, var(--bg-light) 0%, var(--bg-light) 40%, var(--bg-blush) 52%, var(--satin-light) 62%);
  }
  .brand {
    position: absolute;
    left: 30px;
    top: 14px;
    width: 180px;
    height: 120px;
    display: flex;
    flex-direction: column;
    align-items: center;
    justify-content: center;
    gap: 14px;
  }
  .brand-mark {
    width: 62px;
    height: 62px;
    border-radius: 10px;
    background: linear-gradient(135deg, var(--pink), var(--pink-deep));
  }
  .brand-name {
    font-family: "Josefin Sans", sans-serif;
    font-weight: 300;
    font-size: 24px;
    letter-spacing: 3px;
    color: var(--logo-ink);
  }
  .cta {
    position: absolute;
    left: 239px;
    top: 21px;
    width: 277px;
    height: 66px;
    border-radius: 33px;
    background: var(--ink);
    color: var(--white);
    display: flex;
    align-items: center;
    justify-content: center;
    gap: 12px;
    font-family: "Montserrat", sans-serif;
    font-weight: 700;
    font-size: 21px;
    letter-spacing: 0.3px;
    text-decoration: none;
  }
  .cta-arrow { width: 20px; height: 16px; }
  .tagline {
    position: absolute;
    left: 239px;
    top: 106px;
    width: 277px;
    text-align: center;
    font-family: "Montserrat", sans-serif;
    font-weight: 600;
    font-size: 19px;
    letter-spacing: 0.5px;
    color: var(--pink-deep);
  }
  .hero-photo {
    position: absolute;
    left: 560px;
    top: 0;
    width: 640px;
    height: 148px;
    background:
      radial-gradient(ellipse at 40% 55%, rgba(255,220,235,0.6) 0%, rgba(255,220,235,0) 45%),
      radial-gradient(ellipse at 80% 40%, var(--satin-dark) 0%, rgba(184,38,109,0) 55%),
      linear-gradient(90deg, rgba(255,156,201,0) 0%, var(--satin-mid) 25%, var(--satin-light) 60%, var(--satin-mid) 100%);
  }
</style>
</head>
<body>
  <div class="banner">
    <div class="brand">
      <div class="brand-mark"></div>
      <div class="brand-name">VELVETINE</div>
    </div>

    <a class="cta" href="#">
      <span>ESCORT DIRECTORY</span>
      <svg class="cta-arrow" viewBox="0 0 20 16" aria-hidden="true">
        <path d="M1 8 H15 M10 2 L17 8 L10 14" fill="none" stroke="#ffffff" stroke-width="3" stroke-linecap="round" stroke-linejoin="round"/>
      </svg>
    </a>

    <div class="tagline">ADVERTISE FOR FREE</div>

    <div class="hero-photo" role="img" aria-label="Photo of a woman in black lingerie reclining on pink satin sheets"></div>
  </div>
</body>
</html>
```